Your 'not so average' farmers. We are farmers and entrepreneurs trying to connect the great divide.

KTB (Brosmere Holdings Inc) is a family owned farm (in our 3rd generation). We grow vegetables (corn, soy, potatoes, snap beans) but we also invest in and grow businesses. These other businesses can be non-farming related businesses. We are family oriented, environmentally concise, and active in our small community. We need a business card to hand out to our fellow farmers, businesses we would like to partner with and invest in, and community members. So, we need a card with a natural, 'tenders of the land' feel for the farmers but no overly so that we seem centered on farming for the other businesses. We would like it to have our Company info (name, number, email, phone, fax) then Personal info for us five who run the joint (Name, phone, email). So we will order 100 cards for each 5 who work at KTB (500total) that is professional, not boring or hokey, but catching and unique.
Target Market(s)
Farmers, Business Owners, Investors, Community Members
Industry/Entity Type
Farming
Contact Information for Business Card
Office info on one side:
Brosmere Holdings Inc.
1187 Larkin Rd.
Pell Hollow, WI 54872
Office: (608) 555-0417
Fax: (608) 555-0283
brosmereoffice@quillpost.example
Personal Info for the 5 who run KTB. Everybody will have their own personal info on their cards(maybe on the other side):
Name
Mobile
Email
Look and feel

```html
<!DOCTYPE html>
<html lang="en">
<head>
<meta charset="utf-8">
<title>Brosmere Holdings Inc. – Business Card</title>
<link href="https://fonts.googleapis.com/css2?family=Lato:wght@400;700&display=swap" rel="stylesheet">
<style>
  :root {
    --backdrop: #e9e7e1;
    --card-white: #ffffff;
    --ink: #1d1d1b;
    --leaf-green: #b8bb34;
    --leaf-green-deep: #9a9c2a;
    --leaf-line: #6e6a3a;
    --name-white: #ffffff;
  }
  html, body {
    margin: 0;
    padding: 0;
    width: 1200px;
    height: 873px;
    overflow: hidden;
    background: var(--backdrop);
    font-family: "Lato", sans-serif;
  }
  .sheet {
    position: relative;
    width: 1200px;
    height: 873px;
    display: flex;
    align-items: center;
    justify-content: center;
    gap: 60px;
  }
  .card {
    position: relative;
    width: 500px;
    height: 286px;
    box-shadow: 0 2px 10px rgba(0,0,0,0.12);
    overflow: hidden;
  }
  /* personal / office side */
  .card--contact {
    background: var(--card-white);
    color: var(--ink);
    border-bottom: 6px solid var(--leaf-green);
    box-sizing: border-box;
  }
  .contact-block {
    position: absolute;
    top: 58px;
    left: 60px;
    right: 40px;
    text-align: center;
  }
  .person-name {
    font-size: 20px;
    font-weight: 400;
    margin: 0 0 10px;
  }
  .person-line, .office-line {
    font-size: 11.5px;
    line-height: 1.45;
    margin: 0;
  }
  .office-details {
    margin-top: 24px;
  }
  /* brand side */
  .card--brand {
    background: var(--leaf-green);
  }
  .leaf-cluster {
    position: absolute;
  }
  .leaf-cluster--top {
    top: -20px;
    left: -20px;
    width: 330px;
    height: 150px;
    background: radial-gradient(ellipse at 40% 40%, var(--leaf-green-deep) 0%, rgba(154,156,42,0.4) 55%, rgba(184,187,52,0) 75%);
  }
  .leaf-cluster--bottom {
    right: -20px;
    bottom: -20px;
    width: 340px;
    height: 170px;
    background: radial-gradient(ellipse at 60% 60%, var(--leaf-green-deep) 0%, rgba(154,156,42,0.4) 55%, rgba(184,187,52,0) 75%);
  }
  .brand-name {
    position: absolute;
    top: 50%;
    left: 0;
    right: 0;
    transform: translateY(-50%);
    text-align: center;
    font-size: 28px;
    font-weight: 700;
    color: var(--name-white);
    margin: 0;
  }
</style>
</head>
<body>
  <main class="sheet">
    <section class="card card--contact" aria-label="Contact side">
      <div class="contact-block">
        <h1 class="person-name">Dale Mercer</h1>
        <p class="person-line">e-mail: d.mercer@quillpost.example</p>
        <p class="person-line">ph: 0089 55 55 55</p>
        <div class="office-details">
          <p class="office-line">Brosmere Holdings Inc. 1187 Larkin Rd. Pell Hollow, WI 54872</p>
          <p class="office-line">Office: (608) 555-0417 Fax: (608) 555-0283</p>
          <p class="office-line">brosmereoffice@quillpost.example</p>
        </div>
      </div>
    </section>

    <section class="card card--brand" aria-label="Brand side">
      <div class="leaf-cluster leaf-cluster--top" role="img" aria-label="Line-drawn leaf illustration cluster"></div>
      <div class="leaf-cluster leaf-cluster--bottom" role="img" aria-label="Line-drawn leaf illustration cluster"></div>
      <p class="brand-name">Brosmere Holdings Inc</p>
    </section>
  </main>
</body>
</html>
```